Silver Brook Custom Homes business card. Double sided. Modern. professional

Silver Brook Custom Homes
contemporary modern design with our logo /
Double sided with all our contact information
Use same Green colors as in our Logo. Contemporary logo that grabs your attention. Visually pleasing and balanced. Easy to read, and Vibrant. Would love an option for rounded edges. Embossed logo would be amazing.
Contact Information for Business Card
Dana Pellman Owner / General Contractor Silver Brook Custom Homes p: 555.201.0142 m: 555.201.0178 e: silverbrookcustomhomes@mailnest.example w: www.silverbrookcustomhomes.example 218 Wrenfield Mill Road Fernhollow, VT 29088

```html
<!DOCTYPE html>
<html lang="en">
<head>
<meta charset="utf-8">
<title>Silver Brook Custom Homes – Business Card</title>
<link rel="stylesheet" href="https://fonts.googleapis.com/css2?family=Open+Sans:wght@400;600&family=Libre+Baskerville:wght@700&display=swap">
<style>
  :root {
    --backdrop: #e4e2df;
    --card: #f4f4f2;
    --green-dark: #3b5412;
    --green: #4f7a1e;
    --ink: #4a4a4a;
  }
  * { margin: 0; padding: 0; box-sizing: border-box; }
  html, body { width: 1200px; height: 1083px; overflow: hidden; }
  body {
    background: var(--backdrop);
    font-family: "Open Sans", sans-serif;
    display: flex;
    flex-direction: column;
    align-items: center;
    justify-content: center;
    gap: 22px;
  }
  .card {
    position: relative;
    width: 640px;
    height: 355px;
    background: var(--card);
    border-radius: 3px;
    box-shadow: 0 4px 14px rgba(0,0,0,0.14);
  }
  .wordmark {
    font-family: "Open Sans", sans-serif;
    font-weight: 600;
    color: var(--green);
    text-transform: uppercase;
    letter-spacing: 0.08em;
    text-align: center;
    line-height: 1.2;
  }
  .front .wordmark {
    position: absolute;
    left: 0; right: 0; top: 190px;
    font-size: 22px;
  }
  .back .wordmark {
    position: absolute;
    left: 70px; top: 200px;
    width: 200px;
    font-size: 15px;
  }
  .rule-line {
    position: absolute;
    left: 0; right: 0;
    display: flex;
    align-items: center;
    gap: 8px;
    color: var(--green-dark);
    white-space: nowrap;
  }
  .rule-line::before, .rule-line::after {
    content: "";
    flex: 1;
    height: 1.5px;
    background: var(--green-dark);
  }
  .front .rule-line {
    top: 295px;
    font-size: 13px;
    letter-spacing: 0.3em;
  }
  .back .rule-line {
    top: 296px;
    font-size: 13px;
    letter-spacing: 0.02em;
  }
  .contact {
    position: absolute;
    left: 276px; top: 125px;
  }
  .contact-name {
    font-family: "Libre Baskerville", serif;
    font-weight: 700;
    font-size: 18px;
    line-height: 1.2;
    color: var(--green-dark);
    text-transform: uppercase;
  }
  .contact-role {
    font-size: 11px;
    color: var(--ink);
    margin-bottom: 12px;
  }
  .contact-row {
    display: flex;
    align-items: center;
    gap: 7px;
    font-size: 13px;
    color: var(--ink);
    margin-bottom: 5px;
  }
  .contact-row svg { width: 13px; height: 13px; flex: none; }
</style>
</head>
<body>
  <section class="card front">
    <div class="wordmark">Silver Brook Custom Homes</div>
    <div class="rule-line">www.silverbrookcustomhomes.example</div>
  </section>

  <section class="card back">
    <div class="wordmark">Silver Brook<br>Custom Homes</div>
    <div class="contact">
      <div class="contact-name">Dana Pellman</div>
      <div class="contact-role">General Contractor</div>
      <div class="contact-row">
        <svg viewBox="0 0 16 16"><circle cx="8" cy="8" r="8" fill="#3b5412"/><path d="M5.2 4.2l1.4-.3.8 1.9-.9.7a5 5 0 0 0 2.9 2.9l.7-.9 1.9.8-.3 1.4c-3.6.3-6.8-2.9-6.5-6.5z" fill="#fff"/></svg>
        <span>555.201.0142</span>
      </div>
      <div class="contact-row">
        <svg viewBox="0 0 16 16"><circle cx="8" cy="8" r="8" fill="#3b5412"/><rect x="5.5" y="3.5" width="5" height="9" rx="1" fill="none" stroke="#fff" stroke-width="1.2"/><circle cx="8" cy="11" r="0.6" fill="#fff"/></svg>
        <span>555.201.0178</span>
      </div>
      <div class="contact-row">
        <svg viewBox="0 0 16 16"><circle cx="8" cy="8" r="8" fill="#3b5412"/><rect x="4" y="5.2" width="8" height="5.6" fill="#fff"/><path d="M4 5.2l4 3 4-3" fill="none" stroke="#3b5412" stroke-width="0.9"/></svg>
        <span>silverbrookcustomhomes@mailnest.example</span>
      </div>
    </div>
    <div class="rule-line">218 Wrenfield Mill Road Fernhollow, VT 29088</div>
  </section>
</body>
</html>
```